brightpathPRESS is publishing a new book and needs some exceptional cover and layout design!

We are publishing a narrow niche PDF eBook and need both a great cover AND great magazine style layout.

The eBook is a compilation of interviews with 12 financial experts on a particular topic. So the format is is the same for each interview 'chapter'

We are looking for a good front cover/document design that will make what is a pretty dry topic, exciting, interesting and easy to read. Basically - magazine style layout.

The specs for the front cover are:

Title:

The Hurdles and Openings Before Bookkeepers and Planners In Expanding Their Pension Practice In 2014 -2015

by Tom Pelliwick

published by brightpathPRESS

The client would like a similar cover to the one I have attached for your reference. (book front cover example). By no means be limited by this design suggestion. The only caveat is that shots of all interview subjects are included (except the author). These have been included in the zip file.

The design for the text should be elegant and consistent with the design of the front cover. Please format the text in pages 1 to 15 to demonstrate you've understood the brief.

Attached files.

1) MS word version of draft book pages 1 to 15
2) copy of the cover my client would like to emulate.

reminder - this is destined to be a PDF eBook - so looking for some nice eye catching magazine style layout in the design. Columns would be fine.

Good luck!

Brent Malloy
brightpathPRESS

Target Market(s)

Professional Accountants who are running there own businesses

Industry/Entity Type

Financial

Colors

Designer to choose colors to be used in the design.

Requirements
Must have
• The cover must feature headshots of all the interview subjects. The PDF layout must be optimised for viewing on an iPad

```html
<!DOCTYPE html>
<html lang="en">
<head>
<meta charset="utf-8">
<title>The Hurdles &amp; Openings — Book Cover</title>
<link href="https://fonts.googleapis.com/css2?family=Arimo:wght@400;700&display=swap" rel="stylesheet">
<style>
  :root {
    --page-bg: #ffffff;
    --cover-bg: #e6e7e8;
    --band: #737375;
    --strip: #7b7b7d;
    --ink: #333335;
  }
  * { margin: 0; padding: 0; box-sizing: border-box; }
  html, body { width: 1200px; height: 1000px; overflow: hidden; background: var(--page-bg); }
  body { font-family: "Arimo", Arial, sans-serif; color: var(--ink); }
  .canvas { position: relative; width: 1200px; height: 1000px; }
  .cover {
    position: absolute; left: 277px; top: 44px; width: 645px; height: 912px;
    background: var(--cover-bg);
  }
  .band { position: absolute; left: 0; width: 100%; background: var(--band); }
  .band--top { top: 0; height: 18px; }
  .band--bottom { bottom: 0; height: 37px; }
  .centered { position: absolute; left: 0; width: 100%; text-align: center; line-height: 1; }
  .title-the { top: 140px; font-size: 30px; }
  .title-main { font-weight: 700; font-size: 70px; letter-spacing: -0.5px; }
  .title-first { top: 168px; }
  .title-amp { top: 240px; font-size: 22px; }
  .title-second { top: 263px; }
  .subtitle { top: 366px; font-size: 27px; line-height: 33px; }
  .headshots {
    position: absolute; left: 36px; top: 497px; width: 574px; height: 156px;
    background: var(--strip);
    display: grid; grid-template-columns: repeat(8, 62px); grid-auto-rows: 62px;
    column-gap: 8px; row-gap: 7px; padding: 13px 0 0 12px;
  }
  .headshot { width: 62px; height: 62px; }
  .byline { top: 681px; font-size: 24px; }
  .author { top: 712px; font-size: 37px; font-weight: 700; }
  .publisher-label { top: 828px; font-size: 14px; }
  .publisher { top: 846px; font-size: 26px; font-weight: 400; letter-spacing: 0.3px; }
</style>
</head>
<body>
<div class="canvas">
  <div class="cover">
    <div class="band band--top"></div>

    <div class="centered title-the">The</div>
    <div class="centered title-main title-first">Hurdles</div>
    <div class="centered title-amp">&amp;</div>
    <div class="centered title-main title-second">Openings</div>

    <p class="centered subtitle">Before Bookkeepers and Planners In<br>Expanding Their Pension Practice In<br>2014 -2015</p>

    <div class="headshots">
      <div class="headshot" role="img" aria-label="Headshot of interview subject 1" style="background:linear-gradient(#b07a62,#e3c0a8)"></div>
      <div class="headshot" role="img" aria-label="Headshot of interview subject 2" style="background:linear-gradient(#8a8a8a,#3a3a3c)"></div>
      <div class="headshot" role="img" aria-label="Headshot of interview subject 3" style="background:linear-gradient(#5a5a5c,#c59a7e)"></div>
      <div class="headshot" role="img" aria-label="Headshot of interview subject 4" style="background:linear-gradient(#f2f2f2,#c98d6e)"></div>
      <div class="headshot" role="img" aria-label="Headshot of interview subject 5" style="background:linear-gradient(#f0f0f0,#cf9f84)"></div>
      <div class="headshot" role="img" aria-label="Headshot of interview subject 6" style="background:linear-gradient(#ececec,#d7a78c)"></div>
      <div class="headshot" role="img" aria-label="Headshot of interview subject 7" style="background:linear-gradient(#7a7a7a,#c49477)"></div>
      <div class="headshot" role="img" aria-label="Headshot of interview subject 8" style="background:linear-gradient(#d8c8a2,#b98a6c)"></div>
      <div class="headshot" role="img" aria-label="Headshot of interview subject 9" style="background:linear-gradient(#6b8a4a,#c49a7c)"></div>
      <div class="headshot" role="img" aria-label="Headshot of interview subject 10" style="background:linear-gradient(#f1dc94,#eabf9c)"></div>
      <div class="headshot" role="img" aria-label="Headshot of interview subject 11" style="background:linear-gradient(#d9c9b0,#c8a78e)"></div>
      <div class="headshot" role="img" aria-label="Headshot of interview subject 12" style="background:linear-gradient(#cfcfcf,#b88a72)"></div>
      <div class="headshot" role="img" aria-label="Headshot of interview subject 13" style="background:linear-gradient(#d7cdb6,#b98b70)"></div>
      <div class="headshot" role="img" aria-label="Headshot of interview subject 14" style="background:linear-gradient(#f4f4f4,#d8a890)"></div>
      <div class="headshot" role="img" aria-label="Headshot of interview subject 15" style="background:linear-gradient(#f0f0f0,#c99478)"></div>
      <div class="headshot" role="img" aria-label="Headshot of interview subject 16" style="background:linear-gradient(#f4f4f4,#d2a48a)"></div>
    </div>

    <div class="centered byline">by</div>
    <div class="centered author">Tom Pelliwick</div>

    <div class="centered publisher-label">published by</div>
    <div class="centered publisher">brightpathPRESS</div>

    <div class="band band--bottom"></div>
  </div>
</div>
</body>
</html>
```